Skincare at Your Door Logo and business card

We provide dermatological services to the community. This includes Assisted Living Facilities, nursing homes and to large cooperation, Health fairs etc. We provide a health care provider that travels to institutions, providing these services. All procedures and surgeries are done onsite in one of our state of the art mobile clinics. We provide services including, but not limited to; skin biopsies, skin surgeries , surgical procedures including skin cancer removal mole removal and treatment of various skin disorders. we bring mobile Dermatology to you.

Industry/Entity Type

Business

Contact Information for Business Card

Need Logo address phone number, email website

Logo Text

Skincare at Your Door

Logo styles of interest
Emblem Logo
Abstract Logo
Character Logo
Lettermark Logo
Requirements
Must have
• Marcus Hadley ARNP DN-C
• Medical Facilitator
• P. (512) 384-9051
• Fax (619) 532-7140

```html
<!DOCTYPE html>
<html lang="en">
<head>
<meta charset="utf-8">
<title>Skincare at Your Door – Logo and Business Card</title>
<link rel="stylesheet" href="https://fonts.googleapis.com/css2?family=Arimo:ital,wght@0,400;0,700;1,700&family=Roboto+Condensed:ital,wght@1,700&display=swap">
<style>
  :root {
    --navy: #1f3a93;
    --navy-dark: #1c2f6e;
    --teal-blue: #2a4f8a;
    --ink: #3a3a3a;
    --board-top: #ffffff;
    --board-bottom: #cfcfcf;
    --card-white: #ffffff;
    --card-grey-light: #e4e4e4;
    --card-grey: #a9a9a9;
  }
  * { margin: 0; padding: 0; box-sizing: border-box; }
  html, body { width: 1200px; height: 525px; overflow: hidden; }
  body {
    position: relative;
    background: radial-gradient(ellipse 90% 80% at 50% 35%, var(--board-top) 0%, #f0f0f0 55%, var(--board-bottom) 100%);
    font-family: "Arimo", Arial, sans-serif;
  }
  .business-card {
    position: absolute;
    left: 60px; top: 68px;
    width: 525px; height: 357px;
    background: var(--card-white);
    box-shadow: 0 4px 14px rgba(0,0,0,0.35);
    overflow: hidden;
  }
  .card-texture {
    position: absolute;
    left: 0; top: 80px; width: 100%; height: 277px;
    background:
      radial-gradient(ellipse 60% 70% at 55% 40%, rgba(255,255,255,0.7), rgba(255,255,255,0) 70%),
      linear-gradient(180deg, var(--card-grey-light) 0%, #c8c8c8 45%, var(--card-grey) 100%);
  }
  .card-rule { position: absolute; left: 0; top: 0; }
  .card-brand {
    position: absolute;
    left: 318px; top: 40px;
    color: var(--navy);
    font-weight: 700;
    font-size: 24px;
    line-height: 26px;
    letter-spacing: 0.5px;
  }
  .holder-name {
    position: absolute; left: 80px; top: 184px;
    color: var(--navy-dark);
    font-size: 24px; letter-spacing: 0.5px;
    text-transform: uppercase;
  }
  .holder-credentials {
    position: absolute; left: 170px; top: 224px;
    color: var(--teal-blue);
    font-size: 15px;
  }
  .holder-role {
    position: absolute; left: 80px; top: 254px;
    color: var(--ink);
    font-size: 17px;
    text-transform: uppercase;
  }
  .tagline {
    position: absolute; left: 334px; top: 168px;
    color: var(--navy);
    font-family: "Roboto Condensed", "Arial Narrow", sans-serif;
    font-style: italic; font-weight: 700;
    font-size: 22px;
    transform: rotate(-11deg);
    transform-origin: left bottom;
  }
  .phone-icon { position: absolute; left: 330px; top: 238px; }
  .fax-label {
    position: absolute; left: 330px; top: 271px;
    color: var(--navy-dark); font-size: 10px;
  }
  .contact-numbers {
    position: absolute; left: 374px; top: 234px;
    color: var(--navy-dark);
    font-size: 18px; line-height: 21px;
    list-style: none;
  }
  .standalone-logo {
    position: absolute; left: 688px; top: 188px;
    display: flex; align-items: center; gap: 22px;
  }
  .standalone-logo .logo-name {
    color: var(--navy);
    font-weight: 700;
    font-size: 42px;
    line-height: 46px;
    letter-spacing: 1px;
  }
</style>
</head>
<body>
  <section class="business-card" aria-label="Business card">
    <div class="card-texture" role="img" aria-label="Soft grey background with blurred bokeh light spots"></div>
    <svg class="card-rule" width="525" height="120" viewBox="0 0 525 120" aria-hidden="true">
      <line x1="0" y1="80" x2="254" y2="80" stroke="#1f3a93" stroke-width="3"/>
      <circle cx="282" cy="78" r="28" fill="#ffffff" stroke="#1f3a93" stroke-width="3"/>
    </svg>
    <div class="card-brand">Skincare at<br>Your Door</div>

    <div class="holder-name">Marcus Hadley</div>
    <div class="holder-credentials">ARNP DN-C</div>
    <div class="holder-role">Medical Facilitator</div>

    <div class="tagline">Mobile Dermatology</div>

    <svg class="phone-icon" width="26" height="26" viewBox="0 0 26 26" aria-label="Phone">
      <circle cx="13" cy="13" r="11.5" fill="none" stroke="#1c2f6e" stroke-width="1.6"/>
      <path d="M9 7.5c.6-.5 1.4-.4 1.8.2l1.1 1.7c.3.5.2 1.1-.2 1.5l-.7.6c.6 1.4 1.6 2.5 3 3.2l.6-.7c.4-.4 1-.5 1.5-.2l1.7 1.1c.6.4.7 1.2.2 1.8l-.7.8c-.6.6-1.5.8-2.3.5-3.2-1.2-5.6-3.7-6.8-6.9-.3-.8-.1-1.7.5-2.3z" fill="#1c2f6e"/>
    </svg>
    <div class="fax-label">FAX</div>
    <ul class="contact-numbers">
      <li>(512) 384-9051</li>
      <li>(619) 532-7140</li>
    </ul>
  </section>

  <div class="standalone-logo" aria-label="Skincare at Your Door">
    <svg width="100" height="100" viewBox="0 0 100 100" aria-hidden="true">
      <circle cx="50" cy="50" r="46" fill="none" stroke="#1f3a93" stroke-width="5"/>
    </svg>
    <div class="logo-name">Skincare at<br>Your Door</div>
  </div>
</body>
</html>
```